Plastic Business Card for Bookkeeper

We are looking for a simple professional business card design to use for printing on thin frosted plastic (see-through) card stock. Logo and brand guideline documents are attached as well as a photo of our old business card, and another business card example that we like.

Target Market(s)

Small Business

Industry/Entity Type

Bookkeeper

Contact Information for Business Card

Harriet Olsen CPA
Chief Executive Bookkeeper
T. 03 5926 4417
M. 0438 761 205
E. harriet@pinecrestledger.com
W. www.pinecrestledger.com

Font styles to use
Sans Serif

Colors
6b449b
00a990

Requirements
Must have
• Stick with logo colors. Writing should be clear and easy to read and not too cramped together.
Nice to have
• Tag line for back of the card - 'Not your ordinary Bookkeeper'

```html
<!DOCTYPE html>
<html lang="en">
<head>
<meta charset="utf-8">
<title>Pinecrest Ledger – Business Card</title>
<link href="https://fonts.googleapis.com/css2?family=Montserrat:wght@600;700&family=Open+Sans:wght@400&family=Oswald:wght@500&display=swap" rel="stylesheet">
<style>
  :root {
    --brand-purple: #6b449b;
    --brand-teal: #00a990;
    --name-teal: #1a7f8e;
    --ink: #2e2e2e;
    --card-frost: #f3f4f5;
    --backdrop: #dcdde0;
  }
  * { margin: 0; padding: 0; box-sizing: border-box; }
  html, body {
    width: 1200px;
    height: 900px;
    overflow: hidden;
    background: var(--backdrop);
  }
  .business-card {
    position: absolute;
    left: 150px;
    top: 170px;
    width: 900px;
    height: 560px;
    background: var(--card-frost);
    border-radius: 22px 212px 212px 22px / 22px 280px 280px 22px;
    box-shadow: 0 10px 30px rgba(0,0,0,0.12);
  }
  .holder-name {
    position: absolute;
    left: 44px;
    top: 52px;
    font-family: "Montserrat", sans-serif;
    font-weight: 700;
    font-size: 30px;
    color: var(--name-teal);
    letter-spacing: 0.2px;
  }
  .holder-title {
    position: absolute;
    left: 44px;
    top: 92px;
    font-family: "Open Sans", sans-serif;
    font-size: 21px;
    color: var(--ink);
  }
  .contact-list {
    position: absolute;
    left: 44px;
    top: 298px;
    list-style: none;
    font-family: "Open Sans", sans-serif;
    font-size: 22px;
    color: var(--ink);
  }
  .contact-list li {
    display: flex;
    align-items: center;
    height: 33px;
  }
  .contact-icon {
    width: 18px;
    height: 18px;
    margin-right: 8px;
    fill: var(--name-teal);
    flex: none;
  }
  .tagline {
    position: absolute;
    left: 44px;
    top: 462px;
    font-family: "Oswald", sans-serif;
    font-weight: 500;
    font-size: 27px;
    color: var(--brand-purple);
    text-transform: uppercase;
    letter-spacing: 0.2px;
  }
  .brand-mark {
    position: absolute;
    left: 593px;
    top: 130px;
    width: 120px;
    height: 120px;
    border: 9px solid var(--brand-teal);
    border-radius: 50%;
  }
  .brand-name {
    position: absolute;
    left: 433px;
    top: 300px;
    width: 440px;
    text-align: center;
    font-family: "Montserrat", sans-serif;
    font-weight: 700;
    font-size: 36px;
    color: var(--brand-purple);
    letter-spacing: 1px;
    text-transform: uppercase;
  }
</style>
</head>
<body>
  <section class="business-card">
    <h1 class="holder-name">HARRIET OLSEN CPA</h1>
    <p class="holder-title">Chief Executive Bookkeeper</p>

    <ul class="contact-list">
      <li>
        <svg class="contact-icon" viewBox="0 0 20 20"><path d="M2 7c0-3 4-4 8-4s8 1 8 4v2h-4V7H6v2H2z"/><path d="M5 10h10l2 7H3z"/></svg>
        03 5926 4417
      </li>
      <li>
        <svg class="contact-icon" viewBox="0 0 20 20"><path d="M6 1h8a1 1 0 0 1 1 1v16a1 1 0 0 1-1 1H6a1 1 0 0 1-1-1V2a1 1 0 0 1 1-1zm1 2v12h6V3zm3 13a1 1 0 1 0 0 2 1 1 0 0 0 0-2z"/></svg>
        0438 761 205
      </li>
      <li>
        <svg class="contact-icon" viewBox="0 0 20 20"><circle cx="10" cy="10" r="8"/><path d="M6 6c2 0 3 1 3 3s-2 2-2 4M12 4c0 2 2 2 3 4M13 13c1 0 2 1 1 3" stroke="#f3f4f5" stroke-width="1.4" fill="none"/></svg>
        www.pinecrestledger.com
      </li>
      <li>
        <svg class="contact-icon" viewBox="0 0 20 20"><path d="M2 4h16v12H2z"/><path d="M2 4l8 7 8-7" stroke="#f3f4f5" stroke-width="1.4" fill="none"/></svg>
        harriet@pinecrestledger.com
      </li>
    </ul>

    <p class="tagline">Not your ordinary Bookkeeper</p>

    <div class="brand-mark" aria-hidden="true"></div>
    <p class="brand-name">Pinecrest Ledger</p>
  </section>
</body>
</html>
```